Fenwick Stormjays Website

A revamp of the design @ fenwickgridball.com.

Colors and logos must remain same, as does the content and schedules. But we would like a new look to the whole thing.

```html
<!DOCTYPE html>
<html lang="en">
<head>
<meta charset="utf-8">
<title>Fenwick Stormjays</title>
<link href="https://fonts.googleapis.com/css2?family=Arimo:wght@400;700&display=swap" rel="stylesheet">
<style>
:root{
  --dark:#1f1f1f;
  --dark-2:#3a3a3a;
  --purple:#5a0a8c;
  --purple-deep:#3c0466;
  --purple-text:#5b0f88;
  --grey-bar:#cfcfcf;
  --panel:#f4f4f4;
  --ink:#2a2a2e;
  --body:#444;
  --orange:#f26a1b;
}
*{margin:0;padding:0;box-sizing:border-box}
html,body{width:903px;height:1200px;overflow:hidden}
body{position:relative;font-family:"Arimo",Arial,sans-serif;color:var(--ink);
  background:linear-gradient(var(--purple) 0,var(--purple-deep) 800px,var(--purple) 1080px)}
.abs{position:absolute}
.header{left:0;top:0;width:903px;height:120px;background:linear-gradient(var(--dark),var(--dark-2) 60%,#2b2b2b)}
.nav-band{left:0;top:120px;width:903px;height:40px;background:linear-gradient(#6a119f,var(--purple-deep));border-top:1px solid #8a3cc0}
.search-band{left:0;top:160px;width:903px;height:29px;background:linear-gradient(#dcdcdc,#c4c4c4)}
.content{left:97px;top:189px;width:710px;height:891px;background:var(--panel)}
.footer{left:0;top:1100px;width:903px;height:100px;background:linear-gradient(#262626,#141414)}
.logo-box{left:120px;top:0;width:191px;height:176px}
.logo-name{left:120px;top:136px;width:191px;text-align:center;font-weight:700;font-size:16px;color:#111}
.logo-dot{left:188px;top:30px;width:56px;height:56px;border-radius:50%;background:#1c1c1c}
.site-title{left:333px;top:42px;font-size:34px;font-weight:700;color:#fff}
.site-sub{left:333px;top:80px;font-size:19px;color:#bdbdbd}
.more-tab{left:700px;top:0;width:82px;height:17px;background:#f2f2f2;border-radius:0 0 6px 6px;font-size:9px;color:#1a6fa8;padding:3px 0 0 14px}
.nav{left:329px;top:120px;height:40px;display:flex;font-size:9.5px;color:#fff}
.nav span{padding:14px 9px 0}
.nav .active{background:rgba(0,0,0,.25)}
.search{left:648px;top:167px;width:134px;height:17px;background:#fff;border:1px solid #aaa;font-size:8px;font-style:italic;color:#999;padding:3px 4px}
.updated{left:123px;top:198px;font-size:8.5px;color:#333}
.menu-title{left:123px;top:221px;font-size:13px;font-weight:700}
.menu{left:120px;top:246px;width:155px;list-style:none}
.menu li{height:22px;margin-bottom:2.75px;background:linear-gradient(#6e18a8,#4d0680);border-bottom:2px solid #350059;color:#fff;font-size:10px;padding:5px 0 0 17px}
.promo{left:120px;top:729px;width:155px;height:57px;background:var(--orange);border:2px solid #999;color:#fff;font-weight:700;font-size:12px;text-align:center;padding-top:6px;line-height:13px}
.promo .strip{position:absolute;left:0;bottom:0;width:100%;height:16px;background:linear-gradient(90deg,#1c3d8a,#c23,#2a6,#c23)}
.badge{left:120px;top:802px;width:155px;height:55px;background:#e3cfa6;border:2px solid #b07a4a}
.hero{left:292px;top:196px;width:490px;height:290px;border:2px solid #ddd;background:radial-gradient(circle at 45% 40%,#9a3fc4 0,#3a1450 30%,#0d0a12 70%)}
.h-welcome{left:292px;top:510px;font-size:28px;font-weight:700}
.h2{font-size:15px;font-weight:700}
.lead{font-size:13px;color:var(--purple-text);line-height:16px}
.small{font-size:8px;line-height:10.5px;color:#222}
.lorem{left:290px;top:653px;width:494px;font-size:8.5px;line-height:12.8px;color:var(--body)}
.read{font-size:8.5px;color:#222;display:flex;align-items:center;gap:5px}
.arrow{width:12px;height:12px;border-radius:50%;background:#222;color:#fff;font-size:8px;line-height:12px;text-align:center}
.rule{left:292px;top:741px;width:490px;border-top:1px dotted #999}
.card{top:915px;width:211px;height:135px;background:linear-gradient(#f6f6f6,#d8d8d8);border:1px solid #bbb;border-radius:4px}
.card h3{position:absolute;left:10px;top:13px;font-size:13px;color:var(--purple-text)}
.card .icon{position:absolute;left:8px;top:40px;width:64px;height:60px;border-radius:6px}
.card p{position:absolute;left:78px;top:40px;width:122px;font-size:8px;line-height:12.5px;color:#555;text-align:justify}
.card .read{position:absolute;right:20px;top:110px;font-weight:700}
.foot-org{left:104px;top:1110px;font-size:10px;color:#ccc}
.foot-meta{left:104px;top:1125px;font-size:8.5px;line-height:12.5px;color:#fff}
.foot-links{left:104px;top:1158px;width:260px;font-size:8.5px;line-height:10.5px;color:#888}
.social{left:680px;width:104px;height:32px;background:linear-gradient(#fafafa,#d6d6d6);border-radius:3px;font-size:11px;font-weight:700;color:#34508f;padding:9px 0 0 34px}
.social i{position:absolute;left:8px;top:7px;width:18px;height:18px;background:#4a66a8}
</style>
</head>
<body>
<div class="abs header"></div>
<div class="abs nav-band"></div>
<div class="abs search-band"></div>
<div class="abs content"></div>
<div class="abs footer"></div>

<svg class="abs logo-box" viewBox="0 0 191 176"><polygon points="0,0 191,0 191,160 95,176 0,160" fill="#ececec" stroke="#cfcfcf"/></svg>
<div class="abs logo-dot"></div>
<div class="abs logo-name">Fenwick Stormjays</div>

<div class="abs site-title">Fenwick Stormjays</div>
<div class="abs site-sub">Fenwick Independent Gridball Association</div>
<div class="abs more-tab">More info ›</div>

<nav class="abs nav"><span class="active">Home</span><span>Go Pro</span><span>Online Registration</span><span>Fundraisers</span><span>Team Tryouts</span><span>Tournaments</span><span>More</span></nav>
<div class="abs search">Type search here....</div>

<div class="abs updated">Last Updated: October 23, 2011</div>
<div class="abs menu-title">FIGA Main Menu</div>
<ul class="abs menu">
<li>Welcome</li><li>Football</li><li>7 on 7 Football</li><li>Cheer</li><li>Calendar</li><li>Division/Leagues</li><li>Teams/Rosters</li><li>Schedules</li><li>Standings</li><li>Game Results</li><li>Contact Info</li><li>Links</li><li>Sponsors</li><li>Tournaments</li><li>Directions</li><li>Photo Albums</li><li>Forms/Handouts</li><li>Our Classifieds</li><li>Administration</li>
</ul>
<div class="abs promo">Access our League<br>Magazine Store<div class="strip" role="img" aria-label="Row of magazine covers"></div></div>
<div class="abs badge" role="img" aria-label="Partner magazine badge"></div>

<div class="abs hero" role="img" aria-label="Football player in purple light on a dark background"></div>

<div class="abs h-welcome">WELCOME</div>
<div class="abs h2" style="left:292px;top:552px">Fenwick Stormjays 2012 Football Season has started.</div>
<div class="abs lead" style="left:292px;top:579px">Come out and see what everybody is talking about!!<br>"Your Fenwick Stormjays"</div>
<div class="abs small" style="left:292px;top:618px">Come enjoy some Football &amp; Cheerleading while supporting your Fenwick Stormjays!<br>Home games are played at Marlow Pike Middle School.</div>
<div class="abs lorem">Lorem ipsum dolor sit amet, consetetur sadipscing elitr, sed diam nonumy eirmod tempor invidunt ut labore et dolore magna aliquyam erat, sed diam voluptua. At vero eos et accusam et justo duo dolores et ea rebum. Stet clita kasd gubergren, no sea takimata sanctus est Lorem ipsum dolor sit amet. Lorem ipsum dolor sit amet, consetetur sadipscing elitr, sed diam nonumy eirmod tempor invidunt ut labore et dolore magna aliquyam erat, sed diam voluptua. At vero eos et accusam et justo duo dolores et ea rebum. Stet clita kasd gubergren, no sea takimata sanctus est Lorem ipsum dolor sit amet.</div>
<div class="abs read" style="left:712px;top:717px">Read more <span class="arrow">›</span></div>
<div class="abs rule"></div>

<div class="abs h2" style="left:292px;top:756px">American Football Season</div>
<div class="abs lead" style="left:292px;top:783px">Lorem ipsum dolor sit amet, consetetur sadipscing elitr, sed diam nonumy<br>eirmod tempor invidunt ut labore et dolore magna aliquyam erat, sed diam voluptua</div>
<div class="abs small" style="left:292px;top:828px;width:490px">Come enjoy some Football &amp; Cheerleading while supporting your Fenwick Stormjays!<br>Home games are played at Marlow Pike Middle School. Lorem ipsum dolor sit amet, consetetur sadipscing elitr, sed diam nonumy eirmod tempor invidunt ut labore et dolore magna aliquyam erat, sed diam voluptua.</div>
<div class="abs read" style="left:712px;top:871px">Read more <span class="arrow">›</span></div>

<div class="abs card" style="left:120px"><h3>2012 Season Info</h3><div class="icon" role="img" aria-label="Clock and calendar icon" style="background:radial-gradient(circle,#e8f0f8,#7fa7d0)"></div><p>Lorem ipsum dolor sit amet, consetetur sadipscing elitr, sed diam nonumy eirmod tempor invidunt ut laboremagna.</p><div class="read">More info <span class="arrow">›</span></div></div>
<div class="abs card" style="left:345px"><h3>Our League</h3><div class="icon" role="img" aria-label="Leather football" style="background:radial-gradient(ellipse,#9a4a2a,#5a2410 70%,transparent 72%)"></div><p>Lorem ipsum dolor sit amet, consetetur sadipscing elitr, sed diam nonumy eirmod tempor invid dolore magna</p><div class="read">More info <span class="arrow">›</span></div></div>
<div class="abs card" style="left:572px"><h3>Video Training</h3><div class="icon" role="img" aria-label="Video player screen" style="background:linear-gradient(#555,#111);height:50px"></div><p>Lorem ipsum dolor sit amet, consetetur sadipscing elitr, sed diam</p><div class="read">More info <span class="arrow">›</span></div></div>

<div class="abs foot-org">Fenwick Independent Gridball Association</div>
<div class="abs foot-meta">Powered by RosterRally.com<br>Copyright © 2012 stormjay.com</div>
<div class="abs foot-links">Home &nbsp;| &nbsp;About Us &nbsp;| &nbsp;Terms &amp; Condition &nbsp;| &nbsp;Fundraisers &nbsp;|<br>Team Tryouts &nbsp;| &nbsp;Tournaments &nbsp;| &nbsp;Help</div>
<div class="abs social" style="top:1112px"><i></i>Friendwall</div>
<div class="abs social" style="top:1148px"><i></i>Chirpline</div>
</body>
</html>
```